Letterhead PT. Bima Raya Lestari Developer

Alo , My Company need a letterhead design for PT. Bima Raya Lestari Developer Real Estate , i need your each other creative design letterhead for my PT.Bima Raya Lestari Developer Real Estate guys
input my data in letterhead :
Address : Komp. Ruko Taman Sari Blok F No. 27
No. Telp : 0778 512 3364 / 0812 4395 7716
Email : bimarayalestari@mailbox-example.com
Website : www.bimarayalestari-example.com

Target Market(s)

Buyer Property Real Estate & Investor

Industry/Entity Type

Real Estate Development

Font styles to use
Serif
Sans Serif

Requirements
Must have
• according to your creative each other guys as long i need
• Address : Komp. Ruko Taman Sari Blok F No. 27
• No. Telp : 0778 512 3364 / 0812 4395 7716
• Email : bimarayalestari@mailbox-example.com
• Website : www.bimarayalestari-example.com
Nice to have
Should not have
• don't want another colour except : white , dark blue n gold suit to our logo developer real estate

```html
<!DOCTYPE html>
<html lang="en">
<head>
<meta charset="utf-8">
<title>Letterhead – PT. Bima Raya Lestari Developer</title>
<link rel="stylesheet" href="https://fonts.googleapis.com/css2?family=Open+Sans:wght@400;600;700&display=swap">
<style>
  :root {
    --navy: #133a5e;
    --gold: #b8722a;
    --gold-light: #c9933f;
    --ink: #1b1b1b;
    --paper: #ffffff;
    --backdrop: #ececec;
  }
  * { margin: 0; padding: 0; box-sizing: border-box; }
  html, body {
    width: 1200px; height: 1105px; overflow: hidden;
    background: var(--backdrop);
    font-family: "Open Sans", Arial, sans-serif;
  }
  .letterhead {
    position: absolute; left: 230px; top: 30px;
    width: 739px; height: 1045px;
    background: var(--paper);
    box-shadow: 0 6px 22px rgba(0,0,0,.12);
    overflow: hidden;
  }
  .corner { position: absolute; left: 0; width: 739px; height: 120px; }
  .corner--top { top: 0; }
  .corner--bottom { bottom: 0; }
  .company-name {
    position: absolute; left: 62px; top: 168px;
    font-size: 17px; font-weight: 700; color: var(--navy);
    letter-spacing: .5px; line-height: 1.3;
  }
  .company-name .mark {
    display: inline-block; width: 12px; height: 12px;
    background: var(--gold); border-radius: 50%;
    margin-right: 8px; vertical-align: 1px;
  }
  .recipient {
    position: absolute; left: 62px; top: 232px;
    font-size: 13px; line-height: 1.35; color: var(--ink);
  }
  .recipient strong { font-weight: 700; }
  .contact {
    position: absolute; left: 420px; top: 212px;
    list-style: none; font-size: 11.5px; color: var(--navy); line-height: 1.9;
  }
  .contact li { display: flex; align-items: center; gap: 8px; }
  .contact svg { width: 11px; height: 11px; flex: none; }
  .date {
    position: absolute; right: 62px; top: 352px;
    font-size: 13px; color: var(--ink);
  }
  .body-text {
    position: absolute; left: 62px; top: 396px; width: 615px;
    font-size: 12.6px; line-height: 1.45; color: var(--ink);
  }
  .body-text p { margin-bottom: 13px; }
  .body-text .justified { text-align: justify; }
  .signoff {
    position: absolute; left: 62px; top: 782px;
    color: var(--ink);
  }
  .signoff .closing { font-size: 12px; margin-bottom: 6px; }
  .signoff .signer { font-size: 17px; font-weight: 700; }
</style>
</head>
<body>
<main class="letterhead">
  <svg class="corner corner--top" viewBox="0 0 739 120" aria-hidden="true">
    <defs>
      <linearGradient id="goldTop" x1="0" y1="0" x2="1" y2="0">
        <stop offset="0" stop-color="var(--gold)"/>
        <stop offset="1" stop-color="var(--gold-light)"/>
      </linearGradient>
    </defs>
    <polygon points="0,0 600,0 60,108" fill="url(#goldTop)"/>
    <polygon points="0,0 60,108 0,96" fill="var(--navy)"/>
  </svg>

  <div class="company-name"><span class="mark"></span>PT. Bima Raya Lestari Developer</div>

  <div class="recipient">
    <strong>Lorem ipsum dolor sit</strong><br>
    amet, consectetuer<br>
    adipiscing elit, sed
  </div>

  <ul class="contact">
    <li><svg viewBox="0 0 12 12"><path d="M2.5 1 L4.5 1 L5 3.5 L3.8 4.5 Q5 7 7.5 8.2 L8.5 7 L11 7.5 L11 9.5 Q10.5 11 9 11 Q1 10 1 3 Q1 1.5 2.5 1Z" fill="var(--gold)"/></svg>0778 512 3364 / 0812 4395 7716</li>
    <li><svg viewBox="0 0 12 12"><rect x="1" y="2.5" width="10" height="7" fill="none" stroke="var(--gold)" stroke-width="1.2"/><path d="M1 2.5 L6 6.5 L11 2.5" fill="none" stroke="var(--gold)" stroke-width="1.2"/></svg>bimarayalestari@mailbox-example.com</li>
    <li><svg viewBox="0 0 12 12"><circle cx="6" cy="6" r="5" fill="none" stroke="var(--gold)" stroke-width="1.1"/><ellipse cx="6" cy="6" rx="2.2" ry="5" fill="none" stroke="var(--gold)" stroke-width="1"/><path d="M1 6 H11" stroke="var(--gold)" stroke-width="1"/></svg>www.bimarayalestari-example.com</li>
    <li><svg viewBox="0 0 12 12"><path d="M6 11.5 Q2 6.5 2 4.5 A4 4 0 0 1 10 4.5 Q10 6.5 6 11.5Z" fill="var(--gold)"/><circle cx="6" cy="4.5" r="1.4" fill="#fff"/></svg>Komp. Ruko Taman Sari Blok F No. 27</li>
  </ul>

  <div class="date">12/06/2018</div>

  <section class="body-text">
    <p>Lorem ipsum dolor sit amet, consectetuer adipiscing elit, sed diam nonummy nibh euismod tincidunt ut laoreet dolore magna aliquam erat volutpat. Ut wisi enim ad minim veniam, quis nostrud exerci tation ullamcorper suscipit lobortis nisl ut aliquip ex ea commodo consequat. Duis autem vel eum iriure dolor in hendrerit in vulputate velit esse molestie consequat, vel illum dolore eu feugiat nulla facilisis at vero eros et accumsan et iusto odio dignissim qui blandit praesent luptatum zzril delenit augue duis dolore te feugait nulla facilisi.</p>
    <p>Lorem ipsum dolor sit amet, cons ectetuer adipiscing elit, sed diam nonummy nibh euismod tincidunt ut laoreet dolore magna aliquam erat volutpat. Ut wisi enim ad minim veniam, quis nostrud exerci tation ullamcorper suscipit lobortis nisl ut aliquip ex ea commodo consequat. Lorem ipsum dolor sit amet, consectetuer adipiscing elit, sed diam nonummy</p>
    <p class="justified">nibh euismod tincidunt ut laoreet dolore magna aliquam erat volutpat. Ut wisi enim ad minim veniam, quis nostrud exerci tation ullamcorper suscipit lobortis nisl ut aliquip ex ea commodo consequat. Duis autem vel eum iriure dolor in hendrerit in vulputate velit esse molestie consequat, vel illum dolore eu feugiat nulla facilisis at vero eros et accumsan et iusto odio dignissim qui blandit praesent luptatum zzril delenit augue duis dolore te feugait nulla facilisi.</p>
    <p>Lorem ipsum dolor sit amet, cons ectetuer adipiscing elit, sed diam nonummy nibh euismod tincidunt ut laoreet dolore magna aliquam erat volutpat. Ut wisi enim ad minim veniam, quis</p>
  </section>

  <div class="signoff">
    <p class="closing">Regarts</p>
    <p class="signer">Daniel Hart</p>
  </div>

  <svg class="corner corner--bottom" viewBox="0 0 739 120" aria-hidden="true">
    <defs>
      <linearGradient id="goldBottom" x1="0" y1="0" x2="1" y2="0">
        <stop offset="0" stop-color="var(--gold-light)"/>
        <stop offset="1" stop-color="var(--gold)"/>
      </linearGradient>
    </defs>
    <polygon points="739,120 139,120 679,12" fill="url(#goldBottom)"/>
    <polygon points="739,120 679,12 739,24" fill="var(--navy)"/>
  </svg>
</main>
</body>
</html>
```